Wellness Thai Massage Geschäft benötigt eine Preis/Info Broschüre

Ein kleines Thai Massage Geschäft in Bayern: Sukonta Thaimassage
Benötigt eine kleine Preisliste, sowie eine kurze Beschreibung vom Unternehmen. Angeboten werden traditionelle Thaimassagen. Der Farbstil soll dem Logo (Anhang) angepasst sein. Alle Bilder außer die Bilder von der Geschäftsführerin sind optional zur Verwendung verfügbar. Mehr Info wie Preise, etc. sind verfügbar auf der Website https://www.sukontathaimassage-beispiel.de/

```html
<!DOCTYPE html>
<html lang="de">
<head>
<meta charset="utf-8">
<title>Sukonta Thaimassage – Info &amp; Preise</title>
<link href="https://fonts.googleapis.com/css2?family=Quicksand:wght@400;500;600;700&display=swap" rel="stylesheet">
<style>
:root{
  --stage:#e9e9eb;
  --wine:#8a1726;
  --wine-dark:#6e0f1c;
  --berry:#a33a52;
  --rose:#c9707f;
  --blush:#e7a6ae;
  --gold:#f2b437;
  --orange:#ec9a3c;
  --white:#ffffff;
  --note:#e3b4bd;
  --price:#f0a6a8;
}
*{margin:0;padding:0;box-sizing:border-box}
html,body{width:1200px;height:835px;overflow:hidden}
body{background:var(--stage);font-family:"Quicksand",sans-serif;color:var(--white);position:relative}
.page{position:absolute;top:62px;width:503px;height:713px;overflow:hidden;
  background:linear-gradient(180deg,var(--wine) 0%,var(--berry) 55%,var(--wine) 100%);
  box-shadow:3px 4px 8px rgba(0,0,0,.25)}
.page--front{left:79px}
.page--back{left:621px}
.page svg.decor{position:absolute;left:0;top:0}
.logo{position:absolute;display:flex;align-items:center;gap:16px}
.logo__mark{background:#f6ecd6;display:block}
.logo__name{font-weight:600;color:var(--gold);letter-spacing:1.5px;text-transform:uppercase;line-height:1.45}
.abs{position:absolute}
.section-title{font-weight:400;color:var(--gold);font-size:20px;line-height:1}
.body-text{font-size:10.6px;line-height:14.4px;font-weight:500;text-align:justify}
.note{font-style:italic;font-size:9px;line-height:13px;color:var(--note)}
.footer{position:absolute;right:11px;bottom:16px;text-align:right}
.footer__name{font-size:18px;font-weight:500;color:var(--wine-dark);line-height:1.1}
.footer__web{font-size:12px;color:var(--white);line-height:1.4}
.footer__contact{font-size:8px;color:var(--white);line-height:1.6;font-weight:600}
.footer__contact svg{vertical-align:-1px}
.headline{font-size:21px;font-weight:400;line-height:30px;color:var(--white)}
.service{position:absolute;width:218px}
.service__title{display:flex;gap:7px;color:var(--orange);font-size:13px;line-height:13px;font-weight:500}
.service__icon{flex:0 0 22px;height:22px;border-radius:50%;background:var(--blush)}
.service__text{font-size:8.6px;line-height:10.1px;font-weight:500;text-align:justify;margin-top:3px}
.service__price{font-size:8.6px;line-height:11px;font-weight:700;color:var(--price);margin-top:11px}
</style>
</head>
<body>

<!-- Front page -->
<section class="page page--front">
  <svg class="decor" width="503" height="713" viewBox="0 0 503 713">
    <path d="M0 0H503V330C430 300 380 330 300 360C220 390 140 370 0 330Z" fill="var(--wine-dark)"/>
    <path role="img" aria-label="Foto: Masseurin bei einer Thai-Massage im Studio" d="M215 0H503V320C440 300 390 320 320 345C290 330 250 260 215 0Z" fill="url(#photoA)"/>
    <path d="M0 120C70 150 160 110 240 50C260 30 270 10 275 0H0Z" fill="var(--wine)"/>
    <path d="M0 400C120 410 210 370 300 350C380 330 440 320 503 345V380C430 360 360 380 280 400C190 420 100 430 0 425Z" fill="var(--rose)" opacity=".7"/>
    <circle cx="74" cy="247" r="66" fill="var(--blush)"/>
    <circle role="img" aria-label="Foto: Buddha-Figur mit Blüten" cx="74" cy="247" r="60" fill="url(#photoB)"/>
    <circle cx="198" cy="272" r="62" fill="var(--blush)"/>
    <circle role="img" aria-label="Foto: Massageöle und heiße Steine" cx="198" cy="272" r="56" fill="url(#photoC)"/>
    <circle role="img" aria-label="Orchideenblüte" cx="283" cy="310" r="28" fill="#e9a2c4"/>
    <path d="M503 610C420 650 380 680 350 713H503Z" fill="var(--blush)"/>
    <circle role="img" aria-label="Orchideenblüte" cx="459" cy="615" r="34" fill="#eab3d0"/>
    <defs>
      <linearGradient id="photoA" x1="0" y1="0" x2="1" y2="1"><stop offset="0" stop-color="#7a2a2a"/><stop offset=".5" stop-color="#b4634f"/><stop offset="1" stop-color="#d9c7b6"/></linearGradient>
      <radialGradient id="photoB"><stop offset="0" stop-color="#8a5a3c"/><stop offset="1" stop-color="#5a2a24"/></radialGradient>
      <radialGradient id="photoC"><stop offset="0" stop-color="#d8cfc2"/><stop offset="1" stop-color="#3c2a2a"/></radialGradient>
    </defs>
  </svg>

  <div class="logo" style="left:8px;top:14px">
    <span class="logo__mark" style="width:60px;height:40px"></span>
    <span class="logo__name" style="font-size:14px">Sukonta<br>Thaimassage</span>
  </div>

  <h2 class="section-title abs" style="left:27px;top:368px">Was ist Thai Massage eigentlich?</h2>
  <p class="body-text abs" style="left:27px;top:402px;width:459px">Thai Massage existiert schon seit ca. über 2500 Jahren welches sich im Laufe der Zeit zu einer effektiven Methode gegen Schmerzzustände und auch Krankheiten entwickelt welches in der heutigen Zeit sogar Kultstatus erreicht hat. Diese thailändische Heilungsmethode verlangt eine professionelle Ausbildung die Hintergrundwissen und langes Training mit sich bringt.</p>

  <h2 class="section-title abs" style="left:27px;top:497px;font-size:22px">Über uns</h2>
  <p class="body-text abs" style="left:27px;top:525px;width:450px;text-align:left">Sukonta Thaimassage legt einen hohen Wert auf die Zufriedenheit und das Wohlbefinden von jedem Kunden. Wenn sie also z.B nach viel Arbeit gestresst sind und Schmerzen an einer bestimmten Region aufgebaut haben, dann sind sie bei uns an der richtigen Adresse. Geführt wird das Massagestudio von Sukonta Maier, die professionell ausgebildet wurde und auch beruflich schon in Deutschland sowie in Thailand viel Erfahrung gesammelt hat. Wir freuen uns schon auf ihren Besuch bei Sukonta Thaimassage!</p>

  <p class="note abs" style="left:27px;top:669px">Bitte erkundigen sie sich hierfür im Geschäft um<br>über ein erweitertes Angebot zu erfahren.</p>

  <footer class="footer">
    <p class="footer__name">Sukonta Thaimassage</p>
    <p class="footer__web">www.sukontathaimassage-beispiel.de</p>
    <p class="footer__contact">
      <svg width="8" height="8" viewBox="0 0 10 10"><circle cx="5" cy="5" r="4.3" fill="none" stroke="#fff"/><path d="M3.4 3c.3 1.8 1.5 3.2 3.3 3.7" stroke="#fff" fill="none"/></svg> 0170 1234567 &nbsp;
      <svg width="8" height="8" viewBox="0 0 10 10"><circle cx="5" cy="5" r="4.3" fill="none" stroke="#fff"/><circle cx="5" cy="5" r="1.6" fill="#fff"/></svg> info@sukonta-beispiel.de<br>
      Musterweg 12 , 83600 Beispielstadt, Deutschland
    </p>
  </footer>
</section>

<!-- Back page -->
<section class="page page--back">
  <svg class="decor" width="503" height="713" viewBox="0 0 503 713">
    <path d="M0 0H503V290C420 260 360 280 300 250C200 200 100 240 0 270Z" fill="var(--wine-dark)"/>
    <path role="img" aria-label="Foto: lächelnde Masseurin bei einer Dehnübung" d="M301 0H503V290C430 270 380 270 330 255C320 200 305 100 301 0Z" fill="url(#photoD)"/>
    <path d="M0 250C90 230 180 240 260 270C350 300 430 300 503 290V330C420 340 340 330 250 300C160 270 80 265 0 280Z" fill="var(--rose)" opacity=".75"/>
    <circle cx="63" cy="207" r="44" fill="var(--blush)"/>
    <circle role="img" aria-label="Foto: heiße Steine und Öle" cx="63" cy="207" r="39" fill="url(#photoE)"/>
    <circle cx="144" cy="207" r="44" fill="var(--blush)"/>
    <circle role="img" aria-label="Foto: Massageraum" cx="144" cy="207" r="39" fill="url(#photoE)"/>
    <circle cx="226" cy="207" r="44" fill="var(--blush)"/>
    <circle role="img" aria-label="Foto: Massageöle" cx="226" cy="207" r="39" fill="url(#photoE)"/>
    <path d="M503 610C420 650 380 680 350 713H503Z" fill="var(--blush)"/>
    <circle role="img" aria-label="Orchideenblüte" cx="459" cy="615" r="34" fill="#eab3d0"/>
    <defs>
      <linearGradient id="photoD" x1="0" y1="0" x2="1" y2="1"><stop offset="0" stop-color="#9a3a3a"/><stop offset=".6" stop-color="#c8875e"/><stop offset="1" stop-color="#e2c08c"/></linearGradient>
      <radialGradient id="photoE"><stop offset="0" stop-color="#b99a80"/><stop offset="1" stop-color="#3b2222"/></radialGradient>
    </defs>
  </svg>

  <div class="logo" style="left:21px;top:21px">
    <span class="logo__mark" style="width:70px;height:48px"></span>
    <span class="logo__name" style="font-size:17px">Sukonta<br>Thaimassage</span>
  </div>

  <h1 class="headline abs" style="left:21px;top:84px">Thailändische<br>Heilungsmethode verlangt</h1>

  <article class="service" style="left:22px;top:275px">
    <h3 class="service__title"><span class="service__icon" role="img" aria-label="Orchideenblüte"></span><span>Traditionelle<br>Thai-Sport Massage</span></h3>
    <p class="service__text">Mit der traditionellen Thai-Massage werden durch Akupressur, Dehnung und Energielinien-Massage Energieblockaden gelöst. Es wird an 10 Energiepunkten und Linien massiert, die für den Einklang von Körper und Geist wichtig sind. Somit wird eine innere Balance und der Fluss der Lebensenergie erreicht</p>
    <p class="service__price">60 Minuten = 54 Euro<br>90 Minuten = 76 Euro</p>
  </article>

  <article class="service" style="left:22px;top:436px">
    <h3 class="service__title"><span class="service__icon" role="img" aria-label="Orchideenblüte"></span><span style="padding-top:4px">Aromaöl Massage</span></h3>
    <p class="service__text">Die Aromaöl Massage ist eine Behandlungsform zur Regeneration und Harmonisierung des gesamten Körpers. Dabei wird das Basisöl mit ätherischen Ölen angereichert. Die Aromatherapie kann anregend oder entspannend abgestimmt werden</p>
    <p class="service__price">60 Minuten = 51 Euro<br>90 Minuten = 72 Euro</p>
  </article>

  <article class="service" style="left:22px;top:577px">
    <h3 class="service__title"><span class="service__icon" role="img" aria-label="Orchideenblüte"></span><span style="padding-top:4px">Hot Stone Massage</span></h3>
    <p class="service__text">Bei der Hot Stone Massage werden angewärmte Vulkansteine entlag der Energielinien angebracht. Durch die abgegebene gespeicherte Wärme wird der Energiefluss und die Blutzirkulation gesteigert. Es kommt im ganzen Körper zu einer Tiefenentspannung</p>
    <p class="service__price">90 Minuten = 83 Euro</p>
  </article>

  <article class="service" style="left:269px;top:275px">
    <h3 class="service__title"><span class="service__icon" role="img" aria-label="Orchideenblüte"></span><span>Fussreflexzonen<br>Massage</span></h3>
    <p class="service__text">Eine Massage für den wohl für den strapaziertesten Körperteil, den Füssen, setzt neue Kräfte frei und verleiht Vitalität</p>
    <p class="service__price">30 Minuten = 35 Euro<br>60 Minuten = 62 Euro</p>
  </article>

  <article class="service" style="left:269px;top:399px">
    <h3 class="service__title"><span class="service__icon" role="img" aria-label="Orchideenblüte"></span><span style="padding-top:4px">Rücken-Thai Massage</span></h3>
    <p class="service__text">Bei dieser Massagetechnik wird größtenteils der Rücken sowie auch Nacken, Hinterkopf, Schulter und Finger involviert. Diese Massage eignet sich besonders falls eines dieser Bereiche verspannt oder Schmerzen verursacht.</p>
    <p class="service__price">30 Minuten = 35 Euro<br>60 Minuten = 72 Euro</p>
  </article>

  <p class="note abs" style="left:266px;top:525px">Bitte erkundigen sie sich hierfür im Geschäft um<br>über ein erweitertes Angebot zu erfahren.</p>

  <footer class="footer">
    <p class="footer__name">Sukonta Thaimassage</p>
    <p class="footer__web">www.sukontathaimassage-beispiel.de</p>
    <p class="footer__contact">
      <svg width="8" height="8" viewBox="0 0 10 10"><circle cx="5" cy="5" r="4.3" fill="none" stroke="#fff"/><path d="M3.4 3c.3 1.8 1.5 3.2 3.3 3.7" stroke="#fff" fill="none"/></svg> 0170 1234567 &nbsp;
      <svg width="8" height="8" viewBox="0 0 10 10"><circle cx="5" cy="5" r="4.3" fill="none" stroke="#fff"/><circle cx="5" cy="5" r="1.6" fill="#fff"/></svg> info@sukonta-beispiel.de<br>
      Musterweg 12 , 83600 Beispielstadt, Deutschland
    </p>
  </footer>
</section>

</body>
</html>
```